ARC COURTS Business Card Project

I'd like to request a business card design for the new company I've launched.
The name of the company is "ARC COURTS" an indoor unmanned tennis practice facility.
We would like to see designs that use our brand identity color in the logo I've attached.
We hope to get the design with modern, luxurious and elegant tone and manner.
We hope the logo should not be too big.

Business card must have elements as below:
- Logo (One of the logos I've attached)
- Name (In Korean Text) : 박 서 준
- Title (In Korean Text) : 대표
- Phone Number : 010-5830-2947
- Email Address : seojun.park@arccourts-example.co.kr
- Website : www.arccourts-example.co.kr
- Instagram : arccourts
- Address (In Korean text) : 경기도 용인시 수지구 풍덕천로 456 미래타워 5층 501호, 502호

Target Market(s)

Tennis amateurs in 20 to 40s

Industry/Entity Type

Sports, Hobby

Contact Information for Business Card

- Logo (One of the logos I've attached) - Name (In Korean Text) : 박 서 준 - Title (In Korean Text) : 대표 - Phone Number : 010-5830-2947 - Email Address : seojun.park@arccourts-example.co.kr - Website : www.arccourts-example.co.kr - Instagram : arccourts - Address (In Korean text) : 경기도 용인시 수지구 풍덕천로 456 미래타워 5층 501호, 502호

Font styles to use
Sans Serif

Requirements
Must have
• Double sided
Nice to have
• Logo with intaglio or relief embossing
Should not have
• Logo should not be too big.

```html
<!DOCTYPE html>
<html lang="ko">
<head>
<meta charset="utf-8">
<title>ARC COURTS Business Card</title>
<link rel="stylesheet" href="https://fonts.googleapis.com/css2?family=Noto+Sans+KR:wght@400;500&family=Poppins:wght@400;500&display=swap">
<style>
  :root {
    --brand-green: #075033;
    --brand-green-light: #0b5e3d;
    --swoosh-grey: #4a4a4c;
    --paper-white: #ffffff;
    --stage: #e6e7e8;
  }
  html, body {
    margin: 0;
    padding: 0;
    width: 1200px;
    height: 1200px;
    overflow: hidden;
    background: var(--stage);
  }
  .canvas {
    position: relative;
    width: 1200px;
    height: 1200px;
  }
  .card {
    position: absolute;
    left: 160px;
    width: 880px;
    height: 520px;
    border-radius: 44px;
    overflow: hidden;
    box-shadow: 0 10px 30px rgba(0,0,0,0.18);
  }
  .card--front { top: 50px; background: var(--paper-white); }
  .card--back {
    top: 630px;
    background: linear-gradient(100deg, var(--brand-green) 0%, var(--brand-green-light) 55%, var(--brand-green) 100%);
  }
  .card__shapes {
    position: absolute;
    inset: 0;
    width: 100%;
    height: 100%;
  }
  .brand-name {
    position: absolute;
    margin: 0;
    font-family: "Poppins", sans-serif;
    font-weight: 500;
    letter-spacing: 0.08em;
    white-space: nowrap;
  }
  .card--front .brand-name {
    left: 200px;
    top: 120px;
    font-size: 58px;
    color: var(--brand-green);
  }
  .card--back .brand-name {
    left: 0;
    right: 0;
    top: 214px;
    text-align: center;
    font-size: 66px;
    color: var(--paper-white);
  }
  .person {
    position: absolute;
    left: 84px;
    top: 402px;
    color: var(--paper-white);
    font-family: "Noto Sans KR", sans-serif;
  }
  .person__name {
    margin: 0;
    font-size: 38px;
    font-weight: 400;
    letter-spacing: 0.06em;
    line-height: 1.1;
  }
  .person__title {
    margin: 4px 0 0;
    font-size: 26px;
    font-weight: 400;
  }
  .divider {
    position: absolute;
    left: 448px;
    top: 362px;
    width: 1px;
    height: 130px;
    background: rgba(255,255,255,0.25);
  }
  .contact {
    position: absolute;
    left: 476px;
    top: 358px;
    width: 380px;
    margin: 0;
    padding: 0;
    list-style: none;
    color: var(--paper-white);
    font-family: "Poppins", "Noto Sans KR", sans-serif;
    font-size: 14.5px;
    line-height: 24px;
  }
  .contact__item {
    display: flex;
    align-items: flex-start;
    gap: 10px;
    white-space: nowrap;
  }
  .contact__item--address {
    white-space: normal;
    font-family: "Noto Sans KR", sans-serif;
    font-size: 14px;
  }
  .contact__icon {
    width: 15px;
    height: 15px;
    flex: none;
    margin-top: 4px;
  }
</style>
</head>
<body>
<main class="canvas">

  <section class="card card--front" aria-label="Business card front">
    <svg class="card__shapes" viewBox="0 0 880 520" preserveAspectRatio="none" aria-hidden="true">
      <path d="M 868 0 C 800 230 470 350 0 330 L 0 350 C 470 372 820 250 880 40 Z" fill="var(--swoosh-grey)"/>
      <path d="M 880 70 C 820 270 470 390 0 372 L 0 520 L 880 520 Z" fill="var(--brand-green)"/>
    </svg>

    <h1 class="brand-name">ARC COURTS</h1>

    <div class="person">
      <p class="person__name">박 서 준</p>
      <p class="person__title">대표</p>
    </div>

    <span class="divider" aria-hidden="true"></span>

    <ul class="contact">
      <li class="contact__item">
        <svg class="contact__icon" viewBox="0 0 24 24" aria-hidden="true">
          <path fill="#fff" d="M6.6 10.8a15.1 15.1 0 0 0 6.6 6.6l2.2-2.2c.3-.3.7-.4 1-.2 1.1.4 2.3.6 3.6.6.6 0 1 .4 1 1V20c0 .6-.4 1-1 1A17 17 0 0 1 3 4c0-.6.4-1 1-1h3.5c.6 0 1 .4 1 1 0 1.3.2 2.5.6 3.6.1.3 0 .7-.2 1z"/>
        </svg>
        010-5830-2947
      </li>
      <li class="contact__item">
        <svg class="contact__icon" viewBox="0 0 24 24" aria-hidden="true">
          <rect x="2" y="5" width="20" height="14" rx="1.5" fill="#fff"/>
          <path d="M2.5 6 12 13l9.5-7" fill="none" stroke="var(--brand-green)" stroke-width="1.6"/>
        </svg>
        seojun.park@arccourts-example.co.kr
      </li>
      <li class="contact__item">
        <svg class="contact__icon" viewBox="0 0 24 24" aria-hidden="true">
          <g fill="none" stroke="#fff" stroke-width="1.8">
            <circle cx="12" cy="12" r="9.5"/>
            <ellipse cx="12" cy="12" rx="4.2" ry="9.5"/>
            <path d="M2.5 12h19"/>
          </g>
        </svg>
        www.arccourts-example.co.kr
      </li>
      <li class="contact__item">
        <svg class="contact__icon" viewBox="0 0 24 24" aria-hidden="true">
          <circle cx="12" cy="12" r="8" fill="#fff"/>
        </svg>
        arccourts
      </li>
      <li class="contact__item contact__item--address">
        <svg class="contact__icon" viewBox="0 0 24 24" aria-hidden="true">
          <path fill="#fff" d="M12 2a7 7 0 0 0-7 7c0 5.2 7 13 7 13s7-7.8 7-13a7 7 0 0 0-7-7zm0 9.5A2.5 2.5 0 1 1 12 6.5a2.5 2.5 0 0 1 0 5z"/>
        </svg>
        <span>경기도 용인시 수지구 풍덕천로 456<br>미래타워 5층 501호, 502호</span>
      </li>
    </ul>
  </section>

  <section class="card card--back" aria-label="Business card back">
    <h2 class="brand-name">ARC COURTS</h2>
  </section>

</main>
</body>
</html>
```